Web Design for TV Mounting & Appliance Repair Company

We need a website design for the homepage and one inner page for a TV Mounting & Appliance Repair company.
The goal is to promote the company's services and provide information about the company.
TV Mounting & Appliance Repair Company Homepage:
-Banner with company name (Braylo) and slogan (e.g. "Your One Stop Shop for TV Mounting and Appliance Repair")
-Overview/content of services offered (TV mounting, appliance repair)
-Call to action buttons (e.g. "Schedule a Service", "Request a Quote")
-Location and contact information (please create a map of East coast of from Maine to Virginia)
Number of Pages Required
2 page
Font styles to use
Colors
Designer to choose colors to be used in the design.
Look and feel
Each slider illustrates characteristics of the customer's brand and the style your logo design should communicate.

```html
<!DOCTYPE html>
<html lang="en">
<head>
<meta charset="utf-8">
<title>Braylo – TV Mounting &amp; Appliance Repair</title>
<link href="https://fonts.googleapis.com/css2?family=Rubik:wght@400;500;600&family=Roboto:ital,wght@0,300;0,400;0,500;0,700;1,300&display=swap" rel="stylesheet">
<style>
:root{
  --orange:#f15a24;
  --ink:#222;
  --text:#444;
  --muted:#666;
  --grey-bg:#eeeeee;
  --dark:#262626;
  --darker:#161616;
  --white:#fff;
}
*{box-sizing:border-box;margin:0;padding:0}
html,body{width:1200px;height:3752px;overflow:hidden}
body{position:relative;background:var(--white);font-family:"Roboto",sans-serif;color:var(--text)}
.abs{position:absolute}
/* header */
.site-header{left:0;top:0;width:1200px;height:85px;background:var(--white)}
.brand{left:112px;top:18px;height:50px;display:flex;align-items:center;gap:10px;font-family:"Rubik",sans-serif;font-weight:600;font-size:34px;color:var(--orange)}
.brand-dot{width:14px;height:14px;border-radius:50%;background:var(--orange)}
.main-nav{right:112px;top:34px;display:flex;gap:27px;font-size:13px;color:var(--ink)}
.main-nav .active{color:var(--orange)}
/* hero */
.hero{left:0;top:85px;width:1200px;height:627px;background:linear-gradient(100deg,#c9cbce 0%,#e6e7e9 40%,#d9dadc 60%,#b7b9bc 100%)}
.hero-tv{left:335px;top:55px;width:595px;height:375px;background:linear-gradient(#2a2b2e,#45464a)}
.hero-title{left:0;top:244px;width:1200px;text-align:center;font-family:"Rubik",sans-serif;font-weight:600;font-size:48px;line-height:60px;color:var(--white)}
.hero-slogan{left:0;top:310px;width:1200px;text-align:center;font-family:"Rubik",sans-serif;font-size:24px;line-height:37px;color:var(--white)}
.btn-solid{background:var(--orange);color:var(--white);font-family:"Rubik",sans-serif;font-weight:500;font-size:14px;text-transform:uppercase;display:flex;align-items:center;justify-content:center;letter-spacing:.3px}
.hero-btn{left:502px;top:404px;width:195px;height:56px}
.slider-dots{left:0;top:670px;width:1200px;display:flex;justify-content:center;gap:5px}
.slider-dots span{width:12px;height:12px;border-radius:50%;border:1.5px solid var(--white)}
.slider-dots .on{background:var(--white)}
/* tv section */
.tv-photo-a{left:105px;top:811px;width:239px;height:399px;background:linear-gradient(160deg,#dfe0e0,#5b5d60 60%,#c9b79c);box-shadow:0 3px 8px rgba(0,0,0,.15)}
.tv-photo-b{left:361px;top:1086px;width:237px;height:399px;background:linear-gradient(180deg,#e2e6e2 0%,#aeb8b2 40%,#2c2d2e 45%,#aeb8b2 70%,#8a5a3a 75%,#a56b42 100%);box-shadow:0 3px 8px rgba(0,0,0,.15)}
.frame-lines{left:0;top:700px}
.sec-title{font-family:"Rubik",sans-serif;font-weight:500;color:var(--orange)}
.tv-title{left:642px;top:845px;width:460px;font-size:33px;line-height:39px}
.tv-copy{left:642px;top:940px;width:445px;font-size:12px;line-height:26.5px;color:var(--text)}
.checklist{left:642px;top:1170px;width:450px;list-style:none;font-size:12.5px;color:var(--text)}
.checklist li{display:flex;gap:12px;line-height:34px}
.checklist svg{flex:none;margin-top:12px}
.size-title{left:642px;top:1361px;font-size:22px}
.size-btn{top:1411px;height:50px;border:1px solid #ccc;font-size:12.5px;color:var(--ink);display:flex;align-items:center;justify-content:center}
/* appliance */
.appliance{left:0;top:1584px;width:598px;height:514px;background:var(--grey-bg)}
.appliance-photo{left:598px;top:1584px;width:602px;height:514px;background:linear-gradient(120deg,#dde3e6 0%,#f2f4f5 45%,#2f6fd0 75%,#e8e8e8 100%)}
.app-title{left:111px;top:1674px;width:460px;font-size:42px;line-height:53px}
.app-copy{left:111px;top:1795px;width:460px;font-size:13px;line-height:25.5px;color:var(--text)}
.app-btn{left:111px;top:1945px;width:314px;height:56px;box-shadow:0 3px 6px rgba(0,0,0,.2)}
/* cta band */
.cta-band{left:0;top:2098px;width:1200px;height:193px;background:var(--orange)}
.cta-title{left:109px;top:2136px;font-family:"Rubik",sans-serif;font-weight:500;font-size:34px;color:var(--white)}
.cta-copy{left:112px;top:2183px;width:580px;font-size:13px;line-height:22.5px;color:var(--white)}
.cta-btn{left:826px;top:2167px;width:231px;height:58px;border:2px solid var(--white);color:var(--white);font-family:"Rubik",sans-serif;font-weight:500;font-size:14px;display:flex;align-items:center;justify-content:center}
/* testimonials */
.t-label{left:0;top:2372px;width:1200px;text-align:center;font-size:20px;color:var(--orange)}
.t-heading{left:0;top:2405px;width:1200px;text-align:center;font-family:"Rubik",sans-serif;font-weight:500;font-size:31px;color:var(--ink)}
.avatar{border-radius:50%;background:linear-gradient(#c8b8a8,#8a97a0)}
.avatar.side{opacity:.4;border:2px solid var(--orange)}
.avatar.main{border:3px solid var(--orange)}
.stars{left:0;top:2620px;width:1200px;display:flex;justify-content:center;gap:1px}
.quote{left:290px;top:2650px;width:620px;text-align:center;font-style:italic;font-weight:300;font-size:22px;line-height:35px;color:var(--ink)}
.arrow{top:2670px}
.t-name{left:0;top:2744px;width:1200px;text-align:center;font-family:"Rubik",sans-serif;font-weight:500;font-size:15px;color:var(--orange)}
.t-place{left:0;top:2766px;width:1200px;text-align:center;font-size:13px;color:var(--ink)}
/* footer */
.footer{left:0;top:3148px;width:1200px;height:604px;background:var(--dark)}
.map-card{left:112px;top:2858px;width:976px;height:516px;background:var(--white);border-radius:16px;box-shadow:0 4px 18px rgba(0,0,0,.15);overflow:hidden}
.map-area{left:0;top:0;width:454px;height:516px;background:#f1f1f1}
.map-shape{left:10px;top:140px;width:434px;height:200px;background:radial-gradient(ellipse at 60% 55%,#a7a7a7 0%,#b3b3b3 55%,rgba(241,241,241,0) 72%)}
.map-title{left:454px;top:150px;width:522px;text-align:center;font-family:"Rubik",sans-serif;font-weight:500;font-size:28px;line-height:41px;color:var(--orange)}
.map-copy{left:488px;top:255px;width:455px;text-align:center;font-size:12.5px;line-height:27.5px;color:var(--text)}
.foot-brand{left:0;top:3448px;width:1200px;display:flex;justify-content:center;align-items:center;gap:12px;font-family:"Rubik",sans-serif;font-weight:600;font-size:48px;color:var(--white)}
.foot-brand .brand-dot{width:18px;height:18px;background:var(--white)}
.foot-nav{left:0;top:3548px;width:1200px;display:flex;justify-content:center;gap:30px;font-size:15px;font-weight:500;color:var(--white)}
.foot-contact{left:0;top:3590px;width:1200px;display:flex;justify-content:center;gap:18px;font-size:15px;font-weight:500;color:var(--white)}
.foot-contact span{display:flex;align-items:center;gap:7px}
.foot-legal{left:0;top:3635px;width:1200px;display:flex;justify-content:center;gap:14px;font-size:14px;color:var(--white)}
.bottom-bar{left:0;top:3695px;width:1200px;height:57px;background:var(--darker)}
.copyright{left:111px;top:3717px;font-size:15px;color:var(--white)}
.social{top:3716px;width:16px;height:16px;border-radius:50%;border:2px solid var(--white)}
</style>
</head>
<body>

<header class="abs site-header">
  <div class="abs brand"><span class="brand-dot"></span>Braylo</div>
  <nav class="abs main-nav">
    <span class="active">Home</span><span>About Us</span><span>Repair Service</span><span>TV Mounting &amp; Installation Service</span><span>Reviews</span><span>Contact</span>
  </nav>
</header>

<section class="abs hero" role="img" aria-label="Two technicians mounting a large flat-screen TV on a white wall between speakers">
  <div class="abs hero-tv"></div>
</section>
<h1 class="abs hero-title">Braylo</h1>
<p class="abs hero-slogan">Your One Stop Shop for TV Mounting<br>and Appliance Repair</p>
<a class="abs btn-solid hero-btn">Get Started</a>
<div class="abs slider-dots"><span></span><span></span><span class="on"></span><span></span><span></span></div>

<div class="abs tv-photo-a" role="img" aria-label="Technician fitting a wall-mounted TV above a fireplace unit"></div>
<div class="abs tv-photo-b" role="img" aria-label="Wall-mounted TV in a living room under a pendant lamp"></div>
<svg class="abs frame-lines" width="620" height="620" viewBox="0 700 620 620" style="pointer-events:none">
  <polyline points="344,877 517,877 517,1086" fill="none" stroke="#222" stroke-width="2"/>
  <polyline points="344,917 558,995 524,1086" fill="none" stroke="#f15a24" stroke-width="2"/>
  <polyline points="183,1210 183,1296 361,1296" fill="none" stroke="#222" stroke-width="2"/>
  <line x1="183" y1="1214" x2="361" y2="1282" stroke="#f15a24" stroke-width="2"/>
</svg>

<h2 class="abs sec-title tv-title">TV Mounting &amp; Installation Service</h2>
<p class="abs tv-copy">Looking for a professional TV mounting and installation service? Look no further than our expert team at Braylo. We specialize in TV mounting and installation, and can help you get your TV up and running in no time. We understand the importance of a well-mounted TV, and will work with you to ensure that your TV is securely mounted and installed. We also offer a variety of TV mounting options, so you can choose the option that best suits your needs. Contact us today to learn more about our TV mounting and installation services.</p>
<ul class="abs checklist">
  <li><svg width="12" height="10" viewBox="0 0 12 10"><path d="M1 5l3.5 3.5L11 1.5" fill="none" stroke="#f15a24" stroke-width="2"/></svg>Installation of customer-supplied TV mounting bracket</li>
  <li><svg width="12" height="10" viewBox="0 0 12 10"><path d="M1 5l3.5 3.5L11 1.5" fill="none" stroke="#f15a24" stroke-width="2"/></svg>Securing the TV and load testing the hardware</li>
  <li><svg width="12" height="10" viewBox="0 0 12 10"><path d="M1 5l3.5 3.5L11 1.5" fill="none" stroke="#f15a24" stroke-width="2"/></svg>Connect TV to multiple video devices within a single room</li>
  <li><svg width="12" height="10" viewBox="0 0 12 10"><path d="M1 5l3.5 3.5L11 1.5" fill="none" stroke="#f15a24" stroke-width="2"/></svg><span>Neatly dress wires and cables so every connection is tidy, hidden and routed the way you want it</span></li>
</ul>
<h3 class="abs sec-title size-title">Select your TV Size</h3>
<a class="abs size-btn" style="left:644px;width:189px">TV Mounting (up to 60")</a>
<a class="abs size-btn" style="left:840px;width:198px">TV Mounting (61" or larger)</a>

<section class="abs appliance"></section>
<div class="abs appliance-photo" role="img" aria-label="Repairman in blue overalls fixing the open back of a TV"></div>
<h2 class="abs sec-title app-title">Appliance Repair Service</h2>
<p class="abs app-copy">If you are in need of appliance repair, our team at Braylo is here to help. We offer a wide range of appliance repair services, including refrigerator repair, oven repair, dishwasher repair, washer/dryer repair, and more. We understand the importance of having working appliances, and will work quickly and efficiently to get your appliances up and running again.</p>
<a class="abs btn-solid app-btn">Start Your Appliance Repair</a>

<section class="abs cta-band"></section>
<h2 class="abs cta-title">Start Scheduling Your Service Today</h2>
<p class="abs cta-copy">Lorem ipsum dolor sit amet, consectetur adipiscing elit, sed do eiusmod tempor incididunt ut labore et dolore magna aliqua. Ut enim ad minim veniam, quis nostrud exercitation ullamco laboris nisi ut aliquip ex ea commodo consequat.</p>
<a class="abs cta-btn">BOOK APPOINTMENT</a>

<p class="abs t-label">Testimonials</p>
<h2 class="abs t-heading">Your Neighbors Are Our Happy Clients</h2>
<div class="abs avatar side" style="left:439px;top:2482px;width:88px;height:88px" role="img" aria-label="Client portrait"></div>
<div class="abs avatar main" style="left:544px;top:2470px;width:112px;height:112px" role="img" aria-label="Client portrait"></div>
<div class="abs avatar side" style="left:671px;top:2482px;width:88px;height:88px" role="img" aria-label="Client portrait"></div>
<div class="abs stars">
  <svg width="90" height="18" viewBox="0 0 90 18">
    <g fill="none" stroke="#f15a24" stroke-width="1.2">
      <path id="st" d="M9 1.5l2.2 4.6 5 .6-3.7 3.4 1 5L9 12.6 4.5 15.1l1-5L1.8 6.7l5-.6z"/>
      <use href="#st" x="15"/><use href="#st" x="30"/><use href="#st" x="45"/><use href="#st" x="60"/><use href="#st" x="75"/>
    </g>
  </svg>
</div>
<p class="abs quote">The tech from Braylo was very thorough and took the time to answer all my questions.</p>
<svg class="abs arrow" style="left:128px" width="34" height="14" viewBox="0 0 34 14"><path d="M33 7H2M8 1L2 7l6 6" fill="none" stroke="#222" stroke-width="1.8"/></svg>
<svg class="abs arrow" style="left:1028px" width="34" height="14" viewBox="0 0 34 14"><path d="M1 7h31M26 1l6 6-6 6" fill="none" stroke="#222" stroke-width="1.8"/></svg>
<p class="abs t-name">DANA R</p>
<p class="abs t-place">Brookhaven, MA</p>

<footer class="abs footer"></footer>
<section class="abs map-card">
  <div class="abs map-area">
    <div class="abs map-shape" role="img" aria-label="Grey county map of the East Coast service region"></div>
  </div>
  <h2 class="abs map-title">Happily Serving Families On<br>The East Coast For Over 25 Years!</h2>
  <p class="abs map-copy">Lorem ipsum dolor sit amet, consectetur adipiscing elit, sed do eiusmod tempor incididunt ut labore et dolore magna aliqua. Ut enim ad minim veniam, quis nostrud exercitation ullamco laboris nisi ut aliquip ex ea commodo consequat. Duis aute irure dolor in reprehenderit</p>
</section>

<div class="abs foot-brand"><span class="brand-dot"></span>Braylo</div>
<nav class="abs foot-nav"><span>Home</span><span>About Us</span><span>Repair Service</span><span>TV Mounting &amp; Installation Service</span><span>Reviews</span><span>Contact</span></nav>
<div class="abs foot-contact">
  <span><svg width="13" height="13" viewBox="0 0 24 24"><path fill="#fff" d="M6.6 10.8a15.1 15.1 0 006.6 6.6l2.2-2.2c.3-.3.7-.4 1-.2 1.1.4 2.300.6 3.6.6.6 0 1 .4 1 1V20c0 .6-.4 1-1 1A17 17 0 013 4c0-.6.4-1 1-1h3.5c.6 0 1 .4 1 1 0 1.3.2 2.5.6 3.6.1.3 0 .7-.2 1z"/></svg>+1 555-014-2290</span>
  <span><svg width="15" height="12" viewBox="0 0 15 12"><rect x="0.5" y="0.5" width="14" height="11" fill="#fff"/><path d="M1 1l6.5 5L14 1" fill="none" stroke="#262626" stroke-width="1.3"/></svg>info@braylo-example.com</span>
</div>
<div class="abs foot-legal"><span>Privacy Policy</span><span>Terms &amp; Conditions</span><span>Shipping Policy</span></div>

<div class="abs bottom-bar"></div>
<p class="abs copyright">© 2022 All Rights Reserved</p>
<span class="abs social" style="left:1042px" aria-label="Social profile"></span>
<span class="abs social" style="left:1070px" aria-label="Social profile"></span>

</body>
</html>
```